E-Book/ Buch-Cover spannenden Liebesroman gesucht.
Zielgruppe
Ich bin Autorin und suche ein ansprechendes Cover für mein E-Book mit dem Titel:
' Schattenhafte Reue'. Es handelt sich um einen spannenden Liebesroman. Die emotionalen Ängste des Protagonisten, stehen neben den offensichtlichen Bedrohungen der Hauptfigur. Beide müssen ihren Weg zu einem Happyend finden. Da der Titel schon etwas „schreit“, sollte das Cover diesen Eindruck eventuell etwas abfedern.
Aufgabenstellung
Kein Kitsch, kein Schnulzencover, es handelt sich bei aller Dramatik trotzdem um einen Liebesroman. Keinen Thriller.

```html
<!DOCTYPE html>
<html lang="de">
<head>
<meta charset="utf-8">
<title>Schattenhafte Reue – Buchumschlag</title>
<link rel="stylesheet" href="https://fonts.googleapis.com/css2?family=Libre+Bodoni:ital,wght@0,400;1,400&family=Prata&display=swap">
<style>
  :root {
    --sky-top: #17292f;
    --sky-mid: #3d6470;
    --sky-haze: #8fa5ad;
    --dusk-rose: #b9877a;
    --dusk-ember: #c6532f;
    --ground: #050506;
    --ink-light: #ffffff;
    --text-soft: #eef2f3;
    --mark-bg: #000000;
  }
  html, body { margin: 0; padding: 0; overflow: hidden; background: var(--ground); }
  .cover-wrap {
    position: relative;
    width: 1200px;
    height: 893px;
    overflow: hidden;
    color: var(--ink-light);
    font-family: "Libre Bodoni", "Bodoni Moda", serif;
  }
  .sky {
    position: absolute;
    top: 0;
    height: 893px;
    background:
      linear-gradient(180deg,
        var(--sky-top) 0%,
        #22404a 22%,
        var(--sky-mid) 42%,
        var(--sky-haze) 60%,
        var(--dusk-rose) 68%,
        var(--dusk-ember) 73%,
        #3a1c17 77%,
        var(--ground) 82%,
        var(--ground) 100%);
  }
  .sky-back { left: 0; width: 558px; }
  .sky-spine { left: 558px; width: 84px; }
  .sky-front { left: 642px; width: 558px; }

  .press-mark {
    position: absolute;
    background: var(--mark-bg);
    color: var(--ink-light);
    font-family: "Libre Bodoni", serif;
    font-size: 15px;
    display: flex;
    align-items: center;
    justify-content: center;
    letter-spacing: 1px;
  }
  .press-mark-back { left: 0; top: 554px; width: 46px; height: 85px; }
  .press-mark-front { left: 1154px; top: 554px; width: 46px; height: 85px; }
  .press-mark-spine { left: 559px; top: 0; width: 83px; height: 45px; }

  .title-small, .title-large, .label, .author-front {
    position: absolute;
    margin: 0;
    font-family: "Prata", "Libre Bodoni", serif;
    font-weight: 400;
    line-height: 1;
    white-space: nowrap;
  }
  .back-title-small { right: 800px; top: 38px; font-size: 31px; }
  .back-title-large { right: 800px; top: 54px; font-size: 96px; letter-spacing: -2px; }

  .front-title-small { right: 26px; top: 92px; font-size: 66px; }
  .front-title-large { right: 26px; top: 118px; font-size: 190px; letter-spacing: -4px; }
  .label { left: 1012px; top: 400px; font-size: 36px; }
  .author-front { left: 756px; top: 770px; font-size: 50px; letter-spacing: -1px; }

  .blurb {
    position: absolute;
    left: 54px;
    top: 164px;
    width: 466px;
    font-size: 13.6px;
    line-height: 25.5px;
    color: var(--text-soft);
  }
  .blurb p { margin: 0 0 25.5px; text-align: justify; }
  .blurb .teaser, .blurb .closing { font-style: italic; text-align: left; }

  .spine-title, .spine-author {
    position: absolute;
    margin: 0;
    font-family: "Prata", serif;
    font-weight: 400;
    line-height: 1;
    white-space: nowrap;
    transform-origin: left top;
    transform: rotate(-90deg);
  }
  .spine-title { left: 574px; top: 568px; font-size: 46px; }
  .spine-author { left: 580px; top: 857px; font-size: 33px; }
</style>
</head>
<body>
<main class="cover-wrap">
  <div class="sky sky-back" role="img" aria-label="Fotografie: Abendhimmel mit Sternen über dunklem Horizont, Silhouette einer Frau mit wehendem Haar und leuchtenden orangen Lichtpunkten"></div>
  <div class="sky sky-spine" role="img" aria-label="Fortsetzung des Abendhimmels auf dem Buchrücken"></div>
  <div class="sky sky-front" role="img" aria-label="Fotografie: Silhouette einer Frau mit wehendem Haar vor Dämmerungshimmel, orange Lichtpunkte fallen zum Boden"></div>

  <h2 class="title-small back-title-small">Schattenhafte</h2>
  <h2 class="title-large back-title-large">Reue</h2>

  <section class="blurb">
    <p class="teaser">Überlege dir gut, wem du von deinen Ängsten erzählst. Denn was geschieht, wenn dein Albtraum plötzlich Wirklichkeit wird?</p>
    <p>Merles Start in einen neuen Lebensabschnitt könnte nicht gelungener sein. Als sie Markus kennenlernt, träumt sie schon bald von einer gemeinsamen Zukunft. Doch plötzlich wird ihre Gefühlswelt auf einen Schlag in ihren Grundfesten erschüttert. Hat sie sich so in ihm geirrt?</p>
    <p>Der Internetforensiker Markus scheut seit Jahren feste Beziehungen. Die ständige Konfrontation mit sexualisierter Gewalt und Missbrauch hat tiefe Spuren hinterlassen. Seine Vergangenheit steht einer Verbindung mit Merle gefährlich im Weg.</p>
    <p class="closing">Verhängnis oder Neuanfang.</p>
  </section>

  <div class="press-mark press-mark-back">b&amp;l</div>
  <div class="press-mark press-mark-spine">b&amp;l</div>
  <div class="press-mark press-mark-front">b&amp;l</div>

  <p class="spine-title">Schattenhafte Reue</p>
  <p class="spine-author">l. k. sternfeld</p>

  <h1 class="title-small front-title-small">Schattenhafte</h1>
  <h1 class="title-large front-title-large">Reue</h1>
  <p class="label">roman</p>
  <p class="author-front">l. k. sternfeld</p>
</main>
</body>
</html>
```